Business Card Design

I run an executive search and head hunting company.
My areas of business is within financial services and I cover, primarily sales and trading.

I am looking for a double sided, black business card and would like to keep the design fairly simple. Name to front and details on the reverse.

I would require a logo - some logo ideas.

*****Just some idea I am playing with - a white out halo over the "i" in Corwin.
A quill or feather somewhere within the layout. Above the Corwin Hale & Tate ? beneath it ? etc......

I have attached something I quite like but the whole creativity and layout is down to you. I am thinking to have the "&" in between Corwin Hale & Tate, maybe white out perhaps and may have it spot gloss uv'd when it comes to print.

I am pretty open minded though !

Target Market(s)

financial services - brokers and investment banking

Industry/Entity Type

Financial

Contact Information for Business Card

Corwin Hale & Tate
No 7 The Yard
31 Poplin Avenue
Brentwood
Essex
CM19 8QT

Telephone - + 44 (0)1277 555 019
Mobile -+ 44 (0) 7700 934 162
email - owen@corwinhaletate.co.uk
web - www.corwinhaletate.co.uk

Owen Tate
Managing Director

Colors

Designer to choose colors to be used in the design.

Requirements
Should not have
• Finance - brokers investment banking.

```html
<!DOCTYPE html>
<html lang="en">
<head>
<meta charset="utf-8">
<title>Corwin Hale &amp; Tate — Business Card</title>
<link rel="stylesheet" href="https://fonts.googleapis.com/css2?family=Source+Sans+3:wght@400;600;700&display=swap">
<style>
  :root {
    --page: #ffffff;
    --card: #141414;
    --card-edge: #2a2a2a;
    --ink-strong: #a9a9ab;
    --ink: #b4b4b6;
    --ink-soft: #9c9c9e;
  }
  * { margin: 0; padding: 0; box-sizing: border-box; }
  html, body {
    width: 1200px; height: 999px; overflow: hidden;
    background: var(--page);
    font-family: "Source Sans 3", "Myriad Pro", Arial, sans-serif;
  }
  .canvas { position: relative; width: 1200px; height: 999px; }
  .card {
    position: absolute; width: 820px; height: 468px;
    background:
      linear-gradient(to bottom, var(--card-edge) 0, var(--card) 14px, var(--card) 100%);
    box-shadow: 0 0 2px rgba(0,0,0,.35);
  }
  .card--front { left: 68px; top: 26px; }
  .card--back { left: 199px; top: 516px; }

  .wordmark {
    position: absolute; left: 100px; top: 188px; width: 620px;
    text-align: center;
    font-weight: 600; font-size: 64px; line-height: 1;
    letter-spacing: 1px; text-transform: uppercase;
    color: var(--ink-strong); white-space: nowrap;
  }
  .holder { position: absolute; left: 52px; top: 358px; }
  .holder__name { font-weight: 700; font-size: 25px; color: var(--ink-strong); line-height: 32px; }
  .holder__role { font-weight: 400; font-size: 20px; color: var(--ink-soft); line-height: 28px; }

  .address { position: absolute; left: 36px; top: 212px; display: flex; align-items: center; }
  .address__icon { width: 24px; height: 36px; margin-right: 21px; }
  .address__lines { font-size: 20px; line-height: 27.5px; color: var(--ink); }

  .divider { position: absolute; left: 376px; top: 198px; width: 6px; height: 118px; }

  .contacts { position: absolute; left: 408px; top: 198px; list-style: none; }
  .contacts li {
    display: flex; align-items: center; height: 27.5px;
    font-size: 20px; color: var(--ink);
  }
  .contacts svg { width: 18px; height: 18px; margin-right: 24px; flex: none; }
</style>
</head>
<body>
<main class="canvas">
  <section class="card card--front">
    <div class="wordmark">Corwin Hale &amp; Tate</div>
    <div class="holder">
      <p class="holder__name">Owen Tate</p>
      <p class="holder__role">Managing Director</p>
    </div>
  </section>

  <section class="card card--back">
    <div class="address">
      <svg class="address__icon" viewBox="0 0 24 36" aria-hidden="true">
        <path d="M12 1C6 1 1.5 5.5 1.5 11.3 1.5 19 12 35 12 35S22.5 19 22.5 11.3C22.5 5.5 18 1 12 1Zm0 14.5a4.3 4.3 0 1 1 0-8.6 4.3 4.3 0 0 1 0 8.6Z" fill="#a7a7a9"/>
      </svg>
      <p class="address__lines">
        Corwin Hale &amp; Tate No 7<br>
        The Yard 31 Poplin Avenue<br>
        Brentwood Essex CM19 8QT
      </p>
    </div>

    <svg class="divider" viewBox="0 0 6 118" preserveAspectRatio="none" aria-hidden="true">
      <path d="M3 0 L4.6 59 L3 118 L1.4 59 Z" fill="#8c8c8e"/>
    </svg>

    <ul class="contacts">
      <li>
        <svg viewBox="0 0 18 18" aria-hidden="true"><path d="M4 2l3 3-1.6 2.2c1 2 2.4 3.4 4.4 4.4L12 10l3 3-2 2.5C7.5 15 3 10.5 2.5 5Z" fill="#a7a7a9"/><path d="M11 3a4 4 0 0 1 4 4M11 .8A6.2 6.2 0 0 1 17.2 7" stroke="#a7a7a9" stroke-width="1.3" fill="none"/></svg>
        + 44 (0)1277 555 019
      </li>
      <li>
        <svg viewBox="0 0 18 18" aria-hidden="true"><rect x="3" y="1" width="12" height="16" rx="2" fill="#a7a7a9"/><rect x="5" y="4" width="8" height="9" fill="#141414"/><path d="M6 12l6-6" stroke="#a7a7a9" stroke-width="1.4"/></svg>
        07700 934 162
      </li>
      <li>
        <svg viewBox="0 0 18 18" aria-hidden="true"><path d="M1 7l8-5 8 5v9H1Z" fill="#a7a7a9"/><path d="M1 7l8 5 8-5" stroke="#141414" stroke-width="1.3" fill="none"/></svg>
        owen@corwinhaletate.co.uk
      </li>
      <li>
        <svg viewBox="0 0 18 18" aria-hidden="true"><circle cx="9" cy="9" r="8" fill="#a7a7a9"/><g stroke="#141414" stroke-width="1" fill="none"><ellipse cx="9" cy="9" rx="3.5" ry="8"/><path d="M1 9h16M2.5 5h13M2.5 13h13M9 1v16"/></g></svg>
        www.corwinhaletate.co.uk
      </li>
    </ul>
  </section>
</main>
</body>
</html>
```